Buch-/eBook-Cover für ein jährlichen Referenzbuchs der Industrie
Zielgruppe
verlag-mentoria ist ein Fachverlag mit Fokus auf Industrie und Technologie. Seit über 30 Jahren entwickeln wir Medienangebote für Technologiemärkte – immer mit dem Ziel, komplexe Inhalte verständlich und ansprechend aufzubereiten.
Unsere Arbeit basiert auf einer echten Begeisterung für Technik. Mit unseren Marken bauen wir Brücken zwischen Anbietern und Anwendern – in Print, digital und auf Events.
Wir veröffentlichen Magazine, organisieren Veranstaltungen und entwickeln für Kunden individuelle Kommunikationskampagnen. Unsere Plattformen sind in ihren Zielbranchen fest etabliert und genießen ein hohes Maß an Vertrauen.
Bei dem ausgeschriebenen Projekt handelt es sich um unser WERKBLICK.next LUMIRANO – Das Referenzbuch der Industrie, welches jährlich erscheint. LUMIRANO ist aus dem polynesischen Sprachraum und steht für Freiraum.
WERKBLICK.next LUMIRANO ist ein Referenzbuch, das den Namen verdient: unkonventionell, hochrelevant, emotional, motivierend. Bewusst umgesetzt als hochwertige Print-Referenzpublikation!
Wandel bestimmt unsere Zeit und verändert unsere Gesellschaft, unsere Unternehmen, uns alle.
Im Wandel liegt Freiraum zur Gestaltung. Gesellschaftlicher Wandel, Technologie-Wandel, Klimawandel, Wertewandel, Führungswandel oder Organisationswandel sind nur einige Beispiele. Wer dabei den Wandel in engen Bahnen denkt, verschenkt Potential. Veränderung braucht Freiraum für neue Ideen und Perspektiven sowie Persönlichkeiten, die diesen nutzen wollen.
Unsere Leserzielgruppe – Vorwärtsdenker und Zukunftsmacher:
Strategische & technische Entscheider in der Industrie: Inhaber, Vorstand, Geschäftsführer, Betriebs- & Werksleiter, Bereichs-, Gruppen-, Abteilungs- und Projektleiter
Redaktionelles Konzept:
Wer gestaltet die Zukunft der Industrie und ihrer Branchen? Und wie?
Wir geben Personen aus der Industrie den Freiraum, ihre P..
Aufgabenstellung
1.) Kurzzusammenfassung der Ausschreibung
Die 6. Ausgabe des jährlichen Referenzbuchs der Industrie, WERKBLICK.next LUMIRANO 2026, erscheint im Oktober 2025. Für das Cover sucht verlag-mentoria neue Vorschläge, die nicht automatisch eine Fortsetzung der vorherigen Titel sind.
2.) Gestalterische & Inhaltliche Anforderungen
• Format: 195x250 mm + 3 mm Anschnitt
• Rücken: ca. 1,3 cm (Stand letzte Publikation 2024)
• Auflösung: Druckqualität, mind. 300 dpi
• Inhaltliche Elemente:
- Cover
LUMIRANO 2026 Schriftzug (Orientierung egal)
{polynesisch: Freiraum}
Untersatz: Das Referenzbuch der Industrie. Für Vorwärtsdenker und Zukunftsmacher.
part of WERKBLICK.next Logo-Balken am unteren Rand (siehe Beispiel-Cover LUMIRANO 2025)
3 Statements (je 100-150 Zeichen mit Leerzeichen), zu verwendende Schrift: Helvetica Neue LT Std
Folgende Statements dienen als Beispiel und müssen im Nachgang noch angepasst werden
ERFOLG DURCH FLEXIBILITÄT: IT-ARCHITEKTUREN UND KI TRANSFORMIEREN UNTERNEHMEN GRUNDLEGEND!
PRODUKTIONSFOOTPRINT DEUTSCHER MITTELSTAND 2030+: REGIONAL, 100 % AUTOMATISIERT, KLIMANEUTRAL!
UNTERNEHMEN, DIE FLEXIBEL UND ADAPTIV SIND, KÖNNEN CHANCEN NUTZEN UND INNOVATIONSFÜHRER BLEIBEN.
- Rücken:
LUMIRANO
Jahreszahl: 2026
Zu verwendende Schrift: Helvetica Neue LT Std
WICHTIG: Die Farbe Orange (0/80/100/0) soll als Wiedererkennung in die Gestaltungen eingebunden werden. Wir geben die Cover der vergangenen Jahre als Beispiel und Orientierung mit, möchten aber abgesehen von der Farbe bewusst in eine neue Richtung gehen. Bei der Orientierung und Platzierung der Schriftzüge gibt es daher keine Vorgaben. Zu den Beispiel-Cover LUMIRANO: https://www.werkblick-verlag.example/de/Lumirano/e-paper
Das Design darf nicht zu überladen sein.

```html
<!DOCTYPE html>
<html lang="de">
<head>
<meta charset="utf-8">
<title>WERKBLICK.next LUMIRANO 2026 – Cover</title>
<link rel="stylesheet" href="https://fonts.googleapis.com/css2?family=Anton&family=Archivo+Black&family=Raleway:wght@400;500;700&display=swap">
<style>
  :root{
    --page:#ffffff;
    --brown:#43140f;
    --orange:#cc5a24;
    --white:#ffffff;
    --title-font:"Anton", "Arial Narrow", sans-serif;
    --statement-font:"Archivo Black", "Arial Black", sans-serif;
    --text-font:"Raleway", "Helvetica Neue", sans-serif;
  }
  *{margin:0;padding:0;box-sizing:border-box;}
  html,body{width:1200px;height:849px;overflow:hidden;background:var(--page);}
  .canvas{position:relative;width:1200px;height:849px;}

  /* ---------- front cover ---------- */
  .cover{
    position:absolute;width:507px;height:654px;background:var(--brown);
    overflow:hidden;box-shadow:3px 4px 8px rgba(0,0,0,.35);
  }
  .cover--main{left:48px;top:66px;}
  .cover--spread{left:272px;top:0;transform:scale(.505);transform-origin:0 0;box-shadow:none;}

  .network-texture{
    position:absolute;inset:0 0 81px 0;
    background:radial-gradient(ellipse at 40% 35%, rgba(120,60,50,.18), rgba(67,20,15,0) 70%);
  }
  .statement{
    position:absolute;left:41px;color:var(--white);z-index:2;
    font-family:var(--statement-font);font-size:9.2px;line-height:12px;letter-spacing:.2px;
  }
  .statement--one{top:85px;}
  .statement--two{top:260px;}
  .statement--three{top:427px;}

  .title{position:absolute;display:block;overflow:visible;}
  .title text{font-family:var(--title-font);fill:var(--orange);}
  .title--top{left:102px;top:120px;width:303px;height:128px;}
  .title--bottom{left:178px;top:280px;width:303px;height:128px;}

  .translation{
    position:absolute;left:404px;top:166px;color:var(--white);
    font-family:var(--text-font);font-size:7px;letter-spacing:.2px;
    writing-mode:vertical-rl;white-space:nowrap;
  }
  .year{
    position:absolute;right:33px;top:474px;color:var(--orange);
    font-family:var(--statement-font);font-size:48px;line-height:1;letter-spacing:1px;
  }
  .tagline{
    position:absolute;right:33px;top:530px;text-align:right;color:var(--white);
    font-family:var(--text-font);font-size:9.4px;line-height:11.2px;
  }
  .brand-band{
    position:absolute;left:0;right:0;bottom:0;height:81px;background:var(--orange);
    display:flex;align-items:center;justify-content:center;gap:5px;color:var(--white);
    font-family:var(--text-font);
  }
  .brand-band .part-of{font-size:9px;font-weight:500;margin-top:4px;}
  .brand-band .brand-name{font-size:15px;font-weight:700;letter-spacing:.3px;}

  /* ---------- wrap-around spread ---------- */
  .spread{
    position:absolute;left:620px;top:259px;width:529px;height:331px;
    background:var(--brown);overflow:hidden;box-shadow:3px 4px 8px rgba(0,0,0,.35);
  }
  .back-cover{position:absolute;left:0;top:0;width:256px;height:331px;}
  .back-title{position:absolute;left:32px;top:32px;width:142px;height:126px;overflow:visible;}
  .back-title text,.back-year text{font-family:var(--title-font);fill:none;stroke:var(--orange);stroke-width:.8;}
  .back-year text{font-family:var(--statement-font);}
  .back-tagline{
    position:absolute;left:32px;top:167px;color:var(--white);
    font-family:var(--text-font);font-size:4.6px;line-height:5.6px;
  }
  .back-year{position:absolute;left:32px;top:184px;width:68px;height:21px;overflow:visible;}
  .back-band{position:absolute;left:0;bottom:0;width:272px;height:44px;background:var(--orange);}
  .spine{position:absolute;left:256px;top:0;width:16px;height:331px;background:var(--orange);}
</style>
</head>
<body>
<main class="canvas">

  <article class="cover cover--main">
    <div class="network-texture" role="img" aria-label="Feines Netzwerk aus Linien und Knotenpunkten im Hintergrund"></div>
    <p class="statement statement--one">FLEXIBEL ZUM ERFOLG:<br>IT UND KI GESTALTEN DIE UNTERNEHMENSZUKUNFT GRUNDLEGEND NEU.</p>
    <svg class="title title--top" viewBox="0 0 303 128"><text x="0" y="128" font-size="139" textLength="303" lengthAdjust="spacingAndGlyphs">LUMI</text></svg>
    <p class="translation">[polynesisch: Freiraum]</p>
    <p class="statement statement--two">PRODUKTIONSFOOTPRINT DES MITTELSTANDS 2030+:<br>REGIONAL VERANKERT.<br>VOLLAUTOMATISIERT.<br>KLIMANEUTRAL.</p>
    <svg class="title title--bottom" viewBox="0 0 303 128"><text x="0" y="128" font-size="139" textLength="303" lengthAdjust="spacingAndGlyphs">RANO</text></svg>
    <p class="statement statement--three">FLEXIBILITÄT, MUT &amp; ANPASSUNGSFÄHIGKEIT:<br>WER DEN WANDEL MITGESTALTET, FÜHRT INNOVATION AN.</p>
    <p class="year">2026</p>
    <p class="tagline">Das Referenzbuch der Industrie.<br>Für Vorwärtsdenker<br>und Zukunftsmacher.</p>
    <footer class="brand-band"><span class="part-of">part of</span><span class="brand-name">WERKBLICK.next</span></footer>
  </article>

  <section class="spread">
    <div class="back-cover">
      <svg class="back-title" viewBox="0 0 142 126">
        <text x="0" y="60" font-size="63" textLength="142" lengthAdjust="spacingAndGlyphs">LUMI</text>
        <text x="0" y="126" font-size="63" textLength="142" lengthAdjust="spacingAndGlyphs">RANO</text>
      </svg>
      <p class="back-tagline">Das Referenzbuch der Industrie.<br>Für Vorwärtsdenker und Zukunftsmacher.</p>
      <svg class="back-year" viewBox="0 0 68 21"><text x="0" y="20" font-size="27" textLength="68" lengthAdjust="spacingAndGlyphs">2026</text></svg>
    </div>
    <div class="back-band"></div>
    <div class="spine"></div>

    <article class="cover cover--spread" aria-label="Vorderseite im Umschlag">
      <div class="network-texture" role="img" aria-label="Feines Netzwerk aus Linien und Knotenpunkten im Hintergrund"></div>
      <p class="statement statement--one">FLEXIBEL ZUM ERFOLG:<br>IT UND KI GESTALTEN DIE UNTERNEHMENSZUKUNFT GRUNDLEGEND NEU.</p>
      <svg class="title title--top" viewBox="0 0 303 128"><text x="0" y="128" font-size="139" textLength="303" lengthAdjust="spacingAndGlyphs">LUMI</text></svg>
      <p class="translation">[polynesisch: Freiraum]</p>
      <p class="statement statement--two">PRODUKTIONSFOOTPRINT DES MITTELSTANDS 2030+:<br>REGIONAL VERANKERT.<br>VOLLAUTOMATISIERT.<br>KLIMANEUTRAL.</p>
      <svg class="title title--bottom" viewBox="0 0 303 128"><text x="0" y="128" font-size="139" textLength="303" lengthAdjust="spacingAndGlyphs">RANO</text></svg>
      <p class="statement statement--three">FLEXIBILITÄT, MUT &amp; ANPASSUNGSFÄHIGKEIT:<br>WER DEN WANDEL MITGESTALTET, FÜHRT INNOVATION AN.</p>
      <p class="year">2026</p>
      <p class="tagline">Das Referenzbuch der Industrie.<br>Für Vorwärtsdenker<br>und Zukunftsmacher.</p>
      <footer class="brand-band"><span class="part-of">part of</span><span class="brand-name">WERKBLICK.next</span></footer>
    </article>
  </section>

</main>
</body>
</html>
```